Ashford Church of Grace (this will be used for new church sign) sign will be 4'x8' and would like also listed Sunday School 9:00am Worship Service 10:30am.

Logo Text

ASHFORD CHURCH OF GRACE

```html
<!DOCTYPE html>
<html lang="en">
<head>
<meta charset="utf-8">
<title>Ashford Church of Grace – Service Times Sign</title>
<link rel="stylesheet" href="https://fonts.googleapis.com/css2?family=Poppins:wght@700;800&family=Bebas+Neue&family=Arimo:wght@700&display=swap">
<style>
  :root {
    --backdrop: #c8c8c8;
    --sign-white: #ffffff;
    --gold: #c6a800;
    --gold-bright: #ecc400;
    --crimson: #b91d43;
    --text-white: #ffffff;
  }
  * { margin: 0; padding: 0; box-sizing: border-box; }
  html, body {
    width: 1200px;
    height: 1200px;
    overflow: hidden;
    background: var(--backdrop);
  }
  .sign {
    position: absolute;
    left: 54px;
    top: 327px;
    width: 1092px;
    height: 545px;
    background: var(--sign-white);
    overflow: hidden;
  }
  .headline {
    position: absolute;
    left: 37px;
    font-family: "Poppins", sans-serif;
    font-weight: 800;
    line-height: 1;
    white-space: nowrap;
  }
  .headline--place {
    top: 14px;
    font-size: 165px;
    letter-spacing: -2px;
    color: var(--gold);
  }
  .headline--church {
    top: 168px;
    font-size: 106px;
    letter-spacing: -1px;
    color: var(--crimson);
  }
  .church-name {
    position: absolute;
    left: 34px;
    top: 406px;
    display: flex;
    align-items: center;
    gap: 16px;
  }
  .church-name__dot {
    width: 58px;
    height: 58px;
    border-radius: 50%;
    background: var(--gold);
    flex: none;
  }
  .church-name__text {
    font-family: "Poppins", sans-serif;
    font-weight: 700;
    font-size: 30px;
    line-height: 1.1;
    color: var(--crimson);
  }
  .service-band {
    position: absolute;
    left: 404px;
    width: 688px;
    display: flex;
    align-items: center;
    padding-left: 28px;
    white-space: nowrap;
  }
  .service-band--school {
    top: 320px;
    height: 78px;
    background: var(--crimson);
  }
  .service-band--worship {
    top: 406px;
    height: 75px;
    background: var(--gold);
  }
  .service-band__label {
    font-family: "Bebas Neue", sans-serif;
    font-size: 68px;
    letter-spacing: -0.5px;
    line-height: 1;
    color: var(--text-white);
    padding-top: 6px;
    margin-right: 18px;
  }
  .service-band__time {
    font-family: "Arimo", sans-serif;
    font-weight: 700;
    font-size: 70px;
    line-height: 1;
  }
  .service-band--school .service-band__time { color: var(--gold-bright); }
  .service-band--worship .service-band__time { color: var(--crimson); }
</style>
</head>
<body>
  <main class="sign">
    <h1>
      <span class="headline headline--place">ASHFORD</span>
      <span class="headline headline--church">CHURCH OF GRACE</span>
    </h1>

    <div class="church-name">
      <span class="church-name__dot"></span>
      <p class="church-name__text">Ashford<br>Church of Grace</p>
    </div>

    <div class="service-band service-band--school">
      <span class="service-band__label">Sunday School</span>
      <span class="service-band__time">9.00AM</span>
    </div>
    <div class="service-band service-band--worship">
      <span class="service-band__label">Worship Service</span>
      <span class="service-band__time">10.30AM</span>
    </div>
  </main>
</body>
</html>
```